Vel Factory Sticker design

Hello, We are a Doner Kebab Factory, We need sticker design for the following:
1-Sticker for the product details. (look to the attached picture) to stick it on the Doner.
2-Lebel Sticker for the product type, for example ( Premium, Standard and Customised). please check the attached picture,
Don't make the design exactly same as the attachment picture, But try to make something that keeps the same idea but deferent.
Use the same colors of the Logo. but for the lebels you can use other colors
Make it professional design.
Target Market(s)
Restaurant and supermarket
Industry/Entity Type
Factory
Look and feel
Each slider illustrates characteristics of the customer's brand and the style your logo design should communicate.

```html
<!DOCTYPE html>
<html lang="en">
<head>
<meta charset="utf-8">
<title>Vel Factory – Premium Label</title>
<link rel="stylesheet" href="https://fonts.googleapis.com/css2?family=Oswald:wght@500;700&family=Roboto:wght@400&display=swap">
<style>
  :root {
    --paper: #ffffff;
    --edge: #d6d6d6;
    --gold: #c6a80a;
    --grade-red: #a3151b;
    --cream: #f5edc4;
    --code-grey: #6a6a6a;
    --white: #ffffff;
  }
  html, body {
    margin: 0;
    padding: 0;
    width: 810px;
    height: 1200px;
    overflow: hidden;
    background: var(--paper);
  }
  .label {
    position: relative;
    width: 810px;
    height: 1200px;
  }
  .label-shape {
    position: absolute;
    inset: 0;
  }
  .brand {
    position: absolute;
    top: 212px;
    left: 0;
    width: 810px;
    display: flex;
    justify-content: center;
    align-items: center;
    gap: 14px;
  }
  .brand-dot {
    width: 26px;
    height: 26px;
    border-radius: 50%;
    background: var(--code-grey);
  }
  .brand-name {
    font-family: "Oswald", sans-serif;
    font-weight: 500;
    font-size: 48px;
    line-height: 1;
    color: var(--code-grey);
    letter-spacing: 2px;
    text-transform: uppercase;
  }
  .grade-title {
    position: absolute;
    top: 400px;
    left: 0;
    width: 810px;
    margin: 0;
    text-align: center;
    font-family: "Oswald", sans-serif;
    font-weight: 700;
    font-size: 98px;
    line-height: 104px;
    color: var(--white);
    letter-spacing: 3px;
  }
  .quality-line {
    position: absolute;
    top: 738px;
    left: 0;
    width: 810px;
    margin: 0;
    text-align: center;
    font-family: "Oswald", sans-serif;
    font-weight: 700;
    font-size: 56px;
    line-height: 62px;
    color: var(--grade-red);
    letter-spacing: 2px;
  }
  .product-code {
    position: absolute;
    left: 318px;
    top: 914px;
    width: 176px;
    height: 176px;
    border-radius: 50%;
    background: var(--cream);
    display: flex;
    align-items: center;
    justify-content: center;
    text-align: center;
    font-family: "Roboto", sans-serif;
    font-size: 27px;
    line-height: 34px;
    color: var(--code-grey);
  }
</style>
</head>
<body>
  <main class="label">
    <svg class="label-shape" width="810" height="1200" viewBox="0 0 810 1200" aria-hidden="true">
      <defs>
        <clipPath id="label-outline">
          <path d="M218,70 H592 Q712,70 712,190 L698,1070 Q698,1180 588,1180 H222 Q112,1180 112,1070 L98,190 Q98,70 218,70 Z"/>
        </clipPath>
      </defs>
      <path d="M218,70 H592 Q712,70 712,190 L698,1070 Q698,1180 588,1180 H222 Q112,1180 112,1070 L98,190 Q98,70 218,70 Z"
            fill="var(--paper)" stroke="var(--edge)" stroke-width="3"/>
      <g clip-path="url(#label-outline)">
        <rect class="grade-band" x="0" y="354" width="810" height="318" fill="var(--gold)"/>
      </g>
    </svg>

    <div class="brand">
      <span class="brand-dot"></span>
      <span class="brand-name">Vel Factory</span>
    </div>

    <h1 class="grade-title">PREMIUM<br>LABEL</h1>

    <p class="quality-line">PREMIUM<br>QUALITY</p>

    <div class="product-code">VFKB027<br>EC</div>
  </main>
</body>
</html>
```